promotional flyer for Valtera Gym

we are after a double sided a5 leaflet to promote our gym, this is to go out to the general public to entice them into getting membership.

gym membership is £30 per month

it should also include the offer of - if you present this leaflet then there will be no joining fee

some of the features of the gym include

strength machines
cardio machines
functional area
sprung floor mat area

Target Market(s)

Adults 16+ who want to go to the gym and workout

Industry/Entity Type

Gym

Font styles to use
Other font styles liked:
• montserrat Regular

Requirements
Must have
• Clean on brand design
• use images supplied by us
Nice to have
• focus on an inclusive experience as the gym will be advertised to everyone
• should also use our "fitter, stronger, Healthier"

```html
<!DOCTYPE html>
<html lang="en">
<head>
<meta charset="utf-8">
<title>Valtera Gym – Membership Leaflet</title>
<link rel="stylesheet" href="https://fonts.googleapis.com/css2?family=Montserrat:wght@400;700&family=Oswald:wght@600;700&display=swap">
<style>
  :root {
    --backdrop: #d9d9d9;
    --paper: #ffffff;
    --ink: #0d0d0d;
    --orange: #e8562a;
    --white: #ffffff;
  }
  * { box-sizing: border-box; margin: 0; padding: 0; }
  html, body {
    width: 1200px; height: 1117px; overflow: hidden;
    background: var(--backdrop);
  }
  .leaflet {
    position: absolute; left: 222px; top: 24px;
    width: 756px; height: 1069px;
    background: var(--paper);
    padding: 20px;
    box-shadow: 0 6px 24px rgba(0,0,0,0.25);
  }
  .leaflet-panel {
    position: relative; width: 100%; height: 100%;
    background: var(--ink);
    overflow: hidden;
  }
  .brand {
    position: absolute; top: 0; left: 0; right: 0; height: 150px;
    display: flex; align-items: center; justify-content: center;
  }
  .brand-name {
    font-family: "Montserrat", sans-serif; font-weight: 700;
    font-size: 38px; color: var(--white); line-height: 1;
  }
  .hero-photo {
    position: absolute; top: 150px; left: 0; right: 0; height: 520px;
    background: linear-gradient(160deg, #4a4c55 0%, #3a3a40 40%, #6b4a2c 75%, #8a5a30 100%);
  }
  .features {
    position: absolute; top: 700px; left: 34px; width: 360px;
  }
  .features-title {
    font-family: "Oswald", sans-serif; font-weight: 700;
    font-size: 26px; color: var(--orange); text-transform: uppercase;
    letter-spacing: 0.5px; line-height: 1.15;
  }
  .features-list { list-style: none; margin-top: 14px; }
  .features-list li {
    display: flex; align-items: center; gap: 14px;
    font-family: "Montserrat", sans-serif; font-weight: 700;
    font-size: 15px; letter-spacing: 1.5px; color: var(--white);
    text-transform: uppercase; margin-bottom: 12px;
  }
  .features-list svg { width: 22px; height: 14px; flex: none; }
  .price-card {
    position: absolute; top: 712px; right: 34px; width: 280px;
    border: 3px solid var(--orange);
    padding: 8px;
  }
  .price-label {
    background: var(--orange); color: var(--ink);
    font-family: "Oswald", sans-serif; font-weight: 700;
    font-size: 24px; text-transform: uppercase; text-align: center;
    padding: 2px 0;
  }
  .price-amount {
    background: var(--ink); color: var(--white);
    font-family: "Oswald", sans-serif; font-weight: 600;
    font-size: 38px; text-align: center; padding: 4px 0 2px;
  }
  .website {
    position: absolute; top: 858px; right: 34px; width: 280px;
    text-align: center;
    font-family: "Montserrat", sans-serif; font-weight: 400;
    font-size: 14px; letter-spacing: 2px; color: var(--white);
  }
  .offer {
    position: absolute; left: 30px; right: 30px; bottom: 40px;
    font-family: "Oswald", sans-serif; font-weight: 700;
    font-size: 27px; color: var(--orange); text-transform: uppercase;
    text-align: center; line-height: 1.15;
  }
</style>
</head>
<body>
  <article class="leaflet">
    <div class="leaflet-panel">
      <header class="brand">
        <h1 class="brand-name">Valtera Gym</h1>
      </header>

      <div class="hero-photo" role="img" aria-label="Photo of two women riding spin bikes in the gym, with rowing machines and a wall mural behind them"></div>

      <section class="features">
        <h2 class="features-title">The features of the gym include</h2>
        <ul class="features-list">
          <li><svg viewBox="0 0 22 14"><path d="M2 1l6 6-6 6M11 1l6 6-6 6" fill="none" stroke="#e8562a" stroke-width="3"/></svg>Strength machines</li>
          <li><svg viewBox="0 0 22 14"><path d="M2 1l6 6-6 6M11 1l6 6-6 6" fill="none" stroke="#e8562a" stroke-width="3"/></svg>Cardio machines</li>
          <li><svg viewBox="0 0 22 14"><path d="M2 1l6 6-6 6M11 1l6 6-6 6" fill="none" stroke="#e8562a" stroke-width="3"/></svg>Functional area</li>
          <li><svg viewBox="0 0 22 14"><path d="M2 1l6 6-6 6M11 1l6 6-6 6" fill="none" stroke="#e8562a" stroke-width="3"/></svg>Sprung floor mat area</li>
        </ul>
      </section>

      <section class="price-card">
        <p class="price-label">Gym membership</p>
        <p class="price-amount">£30 per month</p>
      </section>
      <p class="website">www.valteragym.co.uk</p>

      <p class="offer">If you present this leaflet then there will be no joining fee</p>
    </div>
  </article>
</body>
</html>
```